Financial services firm needs updated web design

Our current website, corvelwealthgroup.example was created by ourselves using templates provided by our website host, Brightlane Hosting. We are looking to get a whole new look and feel to our website that is clean, professional and easy to navigate. The design must be able to be transferred to Brightlane Hosting for hosting (FTP??-outside my area of expertise - sorry) and that the information can be updated and changed by ourselves in the future. I have included our updated logo and our business card design.
Updates
Project Deadline Extended
Reason: Went away on vacation for two weeks.
Target Market(s)
Age 50+ individuals looking for investment, retirement and estate planning guidance.
Industry/Entity Type
Financial
Number of Pages Required
1 page
Font styles to use
Other font styles liked:
- Adobe Caslon Pro
Look and feel

```html
<!DOCTYPE html>
<html lang="en">
<head>
<meta charset="utf-8">
<title>Corvel Wealth Group – Financial Planning Services</title>
<link href="https://fonts.googleapis.com/css2?family=Noto+Sans:ital,wght@0,400;0,700;1,400&display=swap" rel="stylesheet">
<style>
  :root {
    --green: #3bb54a;
    --green-deep: #2f8f3a;
    --charcoal: #323232;
    --ink: #111111;
    --white: #ffffff;
    --link-blue: #0a2cf0;
    --footer-grey: #9a9a9a;
    --brand-green: #4a8c3c;
  }
  * { margin: 0; padding: 0; box-sizing: border-box; }
  html, body { width: 1200px; height: 900px; overflow: hidden; }
  body {
    position: relative;
    background: var(--charcoal);
    font-family: "Noto Sans", Verdana, sans-serif;
    color: var(--white);
  }

  /* Masthead */
  .masthead { position: absolute; left: 0; top: 0; width: 1200px; height: 198px; background: var(--charcoal); }
  .masthead-band { position: absolute; left: 0; top: 0; width: 1200px; height: 188px; background: var(--green-deep); }
  .banknote-collage {
    position: absolute; top: 0; width: 280px; height: 188px;
    background: linear-gradient(135deg, #9fdc98 0%, #49b045 40%, #86d47f 65%, #3d8a38 100%);
  }
  .banknote-collage.left { left: 0; }
  .banknote-collage.right { left: 920px; }
  .wood-panel {
    position: absolute; top: 0; width: 53px; height: 188px;
    background: linear-gradient(90deg, #4a241a, #6b3a2b 30%, #52291e 60%, #6e3b2c 85%, #48231a);
  }
  .wood-panel.left { left: 292px; }
  .wood-panel.right { left: 855px; }
  .brand-plate {
    position: absolute; left: 357px; top: 0; width: 486px; height: 188px;
    background: var(--white);
  }
  .brand-name {
    position: absolute; left: 0; right: 0; top: 112px;
    text-align: center; font-size: 42px; font-weight: 400; line-height: 52px;
    color: var(--brand-green);
  }

  /* Navigation */
  .main-nav { position: absolute; left: 0; top: 198px; width: 1200px; height: 66px; background: var(--green); }
  .main-nav a {
    position: absolute; top: 15px;
    font-size: 26px; line-height: 36px; letter-spacing: 0.02em;
    color: var(--ink); text-decoration: none;
  }
  .main-nav a.current { color: var(--link-blue); }

  /* Contact column */
  .contact-column {
    position: absolute; left: 0; top: 273px; width: 322px; height: 627px;
    background: var(--green); color: var(--ink);
    text-align: center; font-size: 17px; line-height: 21.5px; letter-spacing: 0.08em;
    padding-top: 25px;
  }
  .firm-name { font-weight: 700; letter-spacing: 0.03em; }
  .firm-tagline { font-style: italic; font-size: 15px; letter-spacing: 0.04em; margin-top: -1px; }
  .contact-column address { font-style: normal; margin-top: 20px; }
  .contact-column .phones { margin-top: 22px; }
  .contact-column a { display: block; margin-top: 22px; color: var(--ink); letter-spacing: 0.02em; }

  /* Services */
  .services { position: absolute; left: 345px; top: 299px; width: 510px; }
  .services h1 { font-size: 27px; line-height: 36px; font-weight: 700; letter-spacing: 0.06em; margin-bottom: 18px; }
  .services ul { list-style: none; font-size: 21px; line-height: 27px; letter-spacing: 0.06em; }
  .services li { margin-bottom: 27px; }
  .services li::before { content: "•"; }
  .services .detail { display: block; padding-left: 16px; }

  .currency-photo {
    position: absolute; left: 864px; top: 306px; width: 302px; height: 432px;
    background: linear-gradient(160deg, #f4f4f2 0%, #e6d6d8 30%, #d8dfe6 55%, #e7dcef 75%, #eef0ee 100%);
  }

  .site-footer {
    position: absolute; left: 330px; top: 872px; width: 600px;
    text-align: center; font-size: 15px; line-height: 20px; letter-spacing: 0.06em;
    color: var(--footer-grey);
  }
</style>
</head>
<body>
  <header class="masthead">
    <div class="masthead-band"></div>
    <div class="banknote-collage left" role="img" aria-label="Collage of green-tinted banknotes"></div>
    <div class="wood-panel left"></div>
    <div class="brand-plate"><span class="brand-name">corvelwealthgroup</span></div>
    <div class="wood-panel right"></div>
    <div class="banknote-collage right" role="img" aria-label="Collage of green-tinted banknotes"></div>
  </header>

  <nav class="main-nav">
    <a class="current" href="#" style="left:26px">home</a>
    <a href="#" style="left:141px">calculators</a>
    <a href="#" style="left:349px">mortgage</a>
    <a href="#" style="left:531px">planning</a>
    <a href="#" style="left:705px">rates</a>
    <a href="#" style="left:837px">newsletter</a>
    <a href="#" style="left:1034px">contact us</a>
  </nav>

  <aside class="contact-column">
    <div class="firm-name">Corvel Wealth Group Services<br>Ltd.</div>
    <div class="firm-tagline">Life Insurance &amp; Financial Planning</div>
    <address>2240 Harbour Road,<br>Delta,<br>British Columbia<br>V4M 1K7</address>
    <div class="phones">Telephone: (604)555-0182<br>Fax: (604)555-0187</div>
    <a href="#">ndavies@corvelwealth.example</a>
    <a href="#">johndavies@corvelwealth.example</a>
  </aside>

  <main class="services">
    <h1>Financial Planning Services</h1>
    <ul>
      <li>Individual Financial Planning</li>
      <li>Business Planning Services<span class="detail">- Employee Group Benefits Pensions</span></li>
      <li>Financial Security Planning</li>
      <li>Investment Planning<span class="detail">- Segregated Funds, Term Deposits &amp; GICs</span></li>
      <li>Retirement Planning Services<span class="detail">- RRSPs &amp; Pensions</span></li>
      <li>Tax &amp; Estate Planning</li>
    </ul>
  </main>

  <div class="currency-photo" role="img" aria-label="Photo of Canadian banknotes and coins fanned out"></div>

  <footer class="site-footer">2014 corvelwealthgroup <em>All Rights Reserved</em></footer>
</body>
</html>
```